Mobile friendly Website design

Client is a packaging equipment company that would like a clean, mobile friendly design. They want a different home page than what they have now. The home page should have the traditional sliders, content area, services are and a featured products area. Please provide an internal page design too.

Target Market(s)

Companies who use packaging equipment, shrink wrappers, heat sealers and carton erectors.

Industry/Entity Type

It Company

Number of Pages Required

2 page

Font styles to use
Serif
Sans Serif

Requirements
Must have
• Must have a clean, mobile friendly design.

```html
<!DOCTYPE html>
<html lang="en">
<head>
<meta charset="utf-8">
<title>Halvern Companies – Packaging Equipment</title>
<link href="https://fonts.googleapis.com/css2?family=Montserrat:wght@400;600;700&family=Open+Sans:wght@400;600;700&display=swap" rel="stylesheet">
<style>
:root{
  --red:#b3182c;
  --red-dark:#7e1020;
  --navy:#1c1933;
  --navy-deep:#151228;
  --ink:#222233;
  --muted:#6d6d78;
  --beige:#f4ede7;
  --tile:#efe3dd;
  --line:#e3d7d2;
  --white:#ffffff;
}
*{margin:0;padding:0;box-sizing:border-box}
html,body{width:1200px;height:4072px;overflow:hidden}
body{font-family:"Open Sans",Arial,sans-serif;color:var(--ink);background:var(--white);font-size:14px;position:relative}
.wrap{width:860px;margin:0 auto;position:relative}
h2.section-title{font-family:"Montserrat",Arial,sans-serif;font-weight:600;font-size:24px;letter-spacing:1px;text-align:center;color:var(--ink)}
.title-mark{display:block;margin:10px auto 0;width:70px;height:8px}

/* top bar */
.topbar{height:26px;background:var(--navy);color:#d8d6e4;font-size:11px;display:flex;align-items:center}
.topbar .wrap{display:flex;justify-content:space-between;align-items:center;width:880px}
.topbar .contact span{margin-right:22px;display:inline-flex;align-items:center;gap:5px}
.topbar .right{display:flex;align-items:center;gap:8px}
.social-dot{width:10px;height:10px;background:#b8b5c8;border-radius:2px;display:inline-block}
.quote-btn-sm{background:var(--white);color:var(--red);font-weight:700;font-size:10px;padding:3px 7px;margin-left:8px}

/* header */
.site-header{height:69px;border-bottom:1px solid var(--line)}
.site-header .wrap{display:flex;align-items:center;height:68px;width:880px}
.brand{display:flex;align-items:center;gap:8px;font-family:"Montserrat",Arial,sans-serif;font-weight:700;font-size:22px;color:var(--red);margin-right:30px;white-space:nowrap}
.brand .mark{width:14px;height:14px;border-radius:50%;background:var(--red)}
.main-nav{display:flex;gap:22px;font-family:"Montserrat",Arial,sans-serif;font-size:11px;font-weight:600;color:var(--ink);flex:1;white-space:nowrap}
.search{width:34px;height:34px;border:2px solid var(--red);border-radius:50%;display:flex;align-items:center;justify-content:center;flex:none}

/* hero */
.hero{height:461px;position:relative;background:linear-gradient(120deg,#8a98a3 0%,#c9d3d8 35%,#7d8b96 60%,#b7c2c8 100%)}
.hero-caption{position:absolute;left:176px;top:180px;width:556px;background:rgba(20,20,30,.82);padding:16px 14px;color:var(--white);font-family:"Montserrat",Arial,sans-serif;font-weight:600;font-size:17px;line-height:30px;letter-spacing:.5px}
.hero-arrow{position:absolute;top:210px;width:24px;height:44px;background:#1d1d22;display:flex;align-items:center;justify-content:center}

/* about */
.about{height:381px;background:var(--beige)}
.about .wrap{display:flex;justify-content:space-between;padding-top:70px}
.about-text{width:480px}
.about-text h2{font-family:"Montserrat",Arial,sans-serif;font-size:22px;font-weight:600;margin-bottom:10px}
.about-lead{background:var(--red);color:var(--white);font-size:11px;line-height:15px;padding:8px 10px;margin-bottom:12px}
.about-text p.body{font-size:11px;line-height:16px;color:var(--muted)}
.read-more{display:block;margin-top:10px;font-size:11px;font-weight:700;color:var(--ink)}
.about-photo-frame{position:relative;width:260px;height:250px;margin-top:-8px}
.about-photo{position:absolute;left:12px;top:12px;width:240px;height:230px;background:linear-gradient(180deg,#d9dde2 0%,#b2b4b6 45%,#7b5a52 70%,#e6e6e6 100%)}
.frame-line{position:absolute;background:var(--red)}

/* services */
.services{height:564px;padding-top:42px}
.services-intro{text-align:center;font-size:12px;line-height:18px;color:var(--muted);width:560px;margin:18px auto 0}
.service-grid{display:grid;grid-template-columns:repeat(6,122px);column-gap:25.6px;row-gap:27px;margin-top:38px}
.service-tile{height:146px;background:var(--tile);display:flex;flex-direction:column;align-items:center;justify-content:center;gap:14px;font-size:11px;color:var(--ink)}
.service-tile svg{width:44px;height:44px}

/* banner */
.banner{height:259px;position:relative;background:linear-gradient(120deg,#7e1020 0%,#a8202f 50%,#6d0d1a 100%);color:var(--white);text-align:center}
.banner h3{position:absolute;top:54px;left:0;right:0;font-family:"Montserrat",Arial,sans-serif;font-weight:600;font-size:23px;line-height:36px;letter-spacing:1px}
.btn-dark{display:inline-flex;align-items:center;gap:8px;background:var(--navy-deep);color:var(--white);font-weight:600;font-size:14px;padding:10px 22px;white-space:nowrap}
.banner .btn-dark{position:absolute;top:160px;left:526px}

/* products */
.products{height:928px;padding-top:40px}
.product-grid{display:grid;grid-template-columns:repeat(4,200px);column-gap:20px;row-gap:12px;margin-top:42px}
.product-card{height:378px;border-top:5px solid var(--red);background:var(--white)}
.product-img{height:230px;background:linear-gradient(180deg,#e4e4e6,#c9c9cd)}
.product-card h4{font-family:"Montserrat",Arial,sans-serif;font-size:13px;font-weight:600;line-height:17px;margin:12px 4px 8px}
.product-card p{font-size:11px;line-height:15px;color:var(--muted);margin:0 4px}

/* newsletter */
.newsletter{height:272px;background:linear-gradient(110deg,#8e1222 0%,#b31a2c 50%,#7e0f1e 100%);color:var(--white);text-align:center;padding-top:40px}
.newsletter h2{font-family:"Montserrat",Arial,sans-serif;font-weight:600;font-size:24px;letter-spacing:1px}
.newsletter .sub{font-size:22px;margin-top:34px;opacity:.95}
.news-form{display:flex;justify-content:center;gap:10px;margin-top:22px}
.news-input{width:380px;height:40px;border-bottom:1px solid rgba(255,255,255,.6);text-align:left;font-size:12px;padding:12px 0;opacity:.85}
.news-form .btn-dark{padding:10px 18px;font-size:14px}

/* testimonials */
.testimonials{height:448px;padding-top:44px;position:relative}
.testi-grid{display:grid;grid-template-columns:410px 410px;justify-content:space-between;margin-top:36px}
.testi-card{height:174px;background:var(--tile);padding:26px 24px 20px 64px;position:relative;font-size:11px;line-height:16px;color:var(--muted)}
.quote-mark{position:absolute;left:18px;top:16px;font-family:Georgia,serif;font-size:60px;color:#c88c92;line-height:1}
.testi-person{display:flex;align-items:center;gap:22px;margin-top:26px}
.avatar{width:66px;height:66px;border-radius:50%;background:linear-gradient(180deg,#9a8478,#6a5a52)}
.testi-person strong{display:block;font-family:"Montserrat",Arial,sans-serif;font-size:13px;letter-spacing:1px}
.testi-person span{font-size:11px;color:var(--muted)}
.side-arrow{position:absolute;width:26px;height:26px;border:1px solid #cfcfd4;background:#f4f4f6;display:flex;align-items:center;justify-content:center}

/* brands */
.brands{height:272px;background:#f8f8f9;padding-top:42px;position:relative}
.brand-row{display:flex;justify-content:space-between;align-items:center;margin-top:60px;width:860px}
.brand-name{font-family:"Montserrat",Arial,sans-serif;font-weight:700;font-size:19px;color:#2a2a3c;display:flex;align-items:center;gap:6px}
.brand-name i{width:10px;height:10px;background:var(--red);display:inline-block}

/* footer */
.footer{height:352px;background:var(--navy-deep);color:#cfcde0;padding-top:60px}
.footer .wrap{display:grid;grid-template-columns:220px 220px 220px 200px;width:900px}
.footer h5{font-family:"Montserrat",Arial,sans-serif;font-size:12px;color:var(--white);letter-spacing:1px;font-weight:600}
.footer h5::after{content:"";display:block;width:30px;height:2px;background:var(--red);margin-top:7px}
.f-list{margin-top:20px;font-size:11px;line-height:16px}
.f-list div{display:flex;gap:8px;margin-bottom:8px}
.badge{width:118px;height:82px;background:#eceaf2;margin-top:14px}
.field{width:190px;height:26px;background:#252241;font-size:10px;padding:6px 8px;color:#8e8ba6;margin-top:10px}
.field.tall{height:70px}
.submit{background:var(--red);color:var(--white);font-size:10px;font-weight:700;padding:6px 12px;display:inline-block;margin-top:10px;margin-left:126px}
.faq-item{display:flex;gap:10px;margin-top:16px;font-size:10px;line-height:14px}
.faq-thumb{width:46px;height:36px;flex:none;background:linear-gradient(135deg,#9aa3ad,#5d6570)}
.map{width:200px;height:160px;margin-top:20px;background:linear-gradient(135deg,#e6e4dc,#cfd6c8 60%,#dad6cc)}
.bottom-bar{height:40px;background:var(--navy-deep);border-top:1px solid #2b2846;color:#aaa7c0;font-size:10px}
.bottom-bar .wrap{display:flex;justify-content:space-between;align-items:center;height:39px;width:900px}
.bottom-bar .soc{display:flex;gap:6px;margin-right:50px}
.bottom-bar .soc i{width:24px;height:24px;background:#3460a8;display:inline-block}
.to-top{position:absolute;right:150px;bottom:4px;width:30px;height:30px;background:var(--red);display:flex;align-items:center;justify-content:center}
</style>
</head>
<body>

<div class="topbar">
  <div class="wrap">
    <div class="contact">
      <span><svg width="9" height="9" viewBox="0 0 10 10"><path d="M2 1l2 2-1 1.5c.8 1.4 1.7 2.3 3 3L7.5 6l2 2-1 1.5C4.5 9 1 5.5.5 1.5z" fill="#d8d6e4"/></svg>Call Us: (555) 014 2290</span>
      <span><svg width="10" height="8" viewBox="0 0 10 8"><rect x=".5" y=".5" width="9" height="7" fill="none" stroke="#d8d6e4"/><path d="M.5.5l4.5 4 4.5-4" fill="none" stroke="#d8d6e4"/></svg>sales@halvernpack.com</span>
    </div>
    <div class="right">
      <i class="social-dot"></i><i class="social-dot"></i><i class="social-dot"></i><i class="social-dot"></i>
      <span class="quote-btn-sm">Get a Quote</span>
    </div>
  </div>
</div>

<header class="site-header">
  <div class="wrap">
    <div class="brand"><span class="mark"></span>Halvern</div>
    <nav class="main-nav">
      <span>HOME</span><span>ABOUT US</span><span>PACKAGING PRODUCTS</span><span>PACKAGING EQUIPMENT SPECIALS</span><span>SUPPORT</span><span>CONTACT US</span>
    </nav>
    <div class="search"><svg width="14" height="14" viewBox="0 0 14 14"><circle cx="6" cy="6" r="4.5" fill="none" stroke="#b3182c" stroke-width="1.6"/><path d="M9.3 9.3L13 13" stroke="#b3182c" stroke-width="1.6"/></svg></div>
  </div>
</header>

<section class="hero" role="img" aria-label="Photo of a stainless packaging line in a production hall">
  <div class="hero-caption">RELIABLE PACKAGING UNDER HARSH CONDITIONS FOR<br>THE MEAT, POULTRY AND SEAFOOD INDUSTRIES</div>
  <div class="hero-arrow" style="left:60px"><svg width="10" height="14" viewBox="0 0 10 14"><path d="M8 1L2 7l6 6" fill="none" stroke="#fff" stroke-width="2"/></svg></div>
  <div class="hero-arrow" style="right:60px"><svg width="10" height="14" viewBox="0 0 10 14"><path d="M2 1l6 6-6 6" fill="none" stroke="#fff" stroke-width="2"/></svg></div>
</section>

<section class="about">
  <div class="wrap">
    <div class="about-text">
      <h2>ABOUT US</h2>
      <p class="about-lead">Halvern Packaging Company was established in 1957 by Walter Halvern, working from a desk made up of a door stacked on top of orange crates, one phone and one customer.</p>
      <p class="body">Halvern Packaging Equipment Company attributes its success in the packaging industry to its commitment to customer service. Our factory trained service technicians have over 100 years of combined experience. Halvern Packaging Equipment Company takes pride in providing an immediate response to your service needs. With our commitment to customer service Halvern Packaging has become the packaging leader in the Midwest for equipment sales and packaging supplies.</p>
      <span class="read-more">Read More »</span>
    </div>
    <div class="about-photo-frame">
      <div class="about-photo" role="img" aria-label="Photo of the company office building in winter"></div>
      <div class="frame-line" style="left:0;top:0;width:2px;height:70px"></div>
      <div class="frame-line" style="left:0;top:0;width:70px;height:2px"></div>
      <div class="frame-line" style="right:0;bottom:0;width:2px;height:70px"></div>
      <div class="frame-line" style="right:0;bottom:0;width:70px;height:2px"></div>
    </div>
  </div>
</section>

<section class="services">
  <div class="wrap">
    <h2 class="section-title">OUR SERVICES</h2>
    <svg class="title-mark" viewBox="0 0 70 8"><path d="M0 4h26M44 4h26" stroke="#b3182c" stroke-width="1.5"/><rect x="30" y="1" width="10" height="6" fill="#b3182c"/></svg>
    <p class="services-intro">Halvern Packaging, Inc. was added to the company in 1989 and includes a lineup of premier manufacturers in the packaging industry. We continue to bring the latest in innovative packaging ideas to our customers.</p>
    <div class="service-grid">
      <div class="service-tile"><svg viewBox="0 0 44 44" fill="none" stroke="#b3182c" stroke-width="2"><rect x="8" y="16" width="28" height="20"/><path d="M22 4v12M17 11l5 5 5-5"/></svg>Packaging Equipment</div>
      <div class="service-tile"><svg viewBox="0 0 44 44" fill="none" stroke="#b3182c" stroke-width="2"><circle cx="22" cy="14" r="7"/><path d="M22 21v18M16 32h12"/></svg>Installation</div>
      <div class="service-tile"><svg viewBox="0 0 44 44" fill="none" stroke="#b3182c" stroke-width="2"><path d="M8 36L30 14M28 8l8 8M8 8l28 28"/></svg>Refurbishing</div>
      <div class="service-tile"><svg viewBox="0 0 44 44" fill="none" stroke="#b3182c" stroke-width="2"><circle cx="14" cy="30" r="6"/><path d="M18 26l18-14M30 8l8 6"/></svg>Service / Repairs</div>
      <div class="service-tile"><svg viewBox="0 0 44 44" fill="none" stroke="#b3182c" stroke-width="2"><rect x="10" y="6" width="22" height="30"/><path d="M15 14h12M15 20h12M15 26h8"/><circle cx="33" cy="33" r="5"/></svg>PM Programs</div>
      <div class="service-tile"><svg viewBox="0 0 44 44" fill="none" stroke="#b3182c" stroke-width="2"><circle cx="16" cy="20" r="9"/><circle cx="16" cy="20" r="3"/><path d="M25 24h14v8H16"/></svg>Adhesives</div>
      <div class="service-tile"><svg viewBox="0 0 44 44" fill="none" stroke="#b3182c" stroke-width="2"><path d="M16 8c-5 8-8 12-8 17a8 8 0 0016 0c0-5-3-9-8-17zM30 16c-3 5-5 8-5 11a5 5 0 0010 0c0-3-2-6-5-11z"/></svg>Ink</div>
      <div class="service-tile"><svg viewBox="0 0 44 44" fill="none" stroke="#b3182c" stroke-width="2"><path d="M24 6h14v14L20 38 6 24z"/><circle cx="31" cy="13" r="2.5"/></svg>Labels &amp; Ribbons</div>
      <div class="service-tile"><svg viewBox="0 0 44 44" fill="none" stroke="#b3182c" stroke-width="2"><path d="M8 8l10 4 8 20 12-4"/><circle cx="24" cy="36" r="3"/><rect x="18" y="14" width="12" height="10" transform="rotate(-20 24 19)"/></svg>Packing Supplies</div>
      <div class="service-tile"><svg viewBox="0 0 44 44" fill="none" stroke="#b3182c" stroke-width="2"><path d="M10 6l24 32M34 6L10 38M8 22h28"/></svg>Plastic Strapping</div>
      <div class="service-tile"><svg viewBox="0 0 44 44" fill="none" stroke="#b3182c" stroke-width="2"><circle cx="22" cy="22" r="15"/><circle cx="22" cy="22" r="5"/><path d="M22 7v10M22 27v10M7 22h10M27 22h10"/></svg>Stretch Film</div>
      <div class="service-tile"><svg viewBox="0 0 44 44" fill="none" stroke="#b3182c" stroke-width="2"><rect x="8" y="8" width="28" height="28"/><path d="M22 14v16M14 22h16"/></svg>More</div>
    </div>
  </div>
</section>

<section class="banner" role="img" aria-label="Red tinted photo of packaging machinery">
  <h3>WE ARE THE PACKAGING LEADER IN THE MIDWEST FOR EQUIPMENT<br>SALES AND PACKAGING SUPPLIES!</h3>
  <span class="btn-dark">Get a Quote <svg width="8" height="10" viewBox="0 0 8 10"><path d="M1 1l5 4-5 4" fill="none" stroke="#fff" stroke-width="2"/></svg></span>
</section>

<section class="products">
  <div class="wrap">
    <h2 class="section-title">FEATURED PRODUCTS</h2>
    <svg class="title-mark" viewBox="0 0 70 8"><path d="M0 4h26M44 4h26" stroke="#b3182c" stroke-width="1.5"/><rect x="30" y="1" width="10" height="6" fill="#b3182c"/></svg>
    <div class="product-grid">
      <article class="product-card"><div class="product-img" role="img" aria-label="Product photo of a stretch wrapper"></div><h4>Stratos W-240 Stretch Wrapper</h4><p>Eliminate the "run-around" with Easy Motion™ in a fast-paced environment […]</p></article>
      <article class="product-card"><div class="product-img" role="img" aria-label="Product photo of a spindle wrap labeler"></div><h4>RTX-6 Spindle Wrap Labeler</h4><p>The RTX-4 Top &amp; Bottom Labeler is built to automatically pressure sensitive labels […]</p></article>
      <article class="product-card"><div class="product-img" role="img" aria-label="Product photo of a gallon wrap labeler"></div><h4>RTX-8 Gallon Wrap Labeler</h4><p>The RTX-8 Gallon Wrap Labeler is built to automatically apply pressure sensitive labels […]</p></article>
      <article class="product-card"><div class="product-img" role="img" aria-label="Product photo of colored carton sealing tape rolls"></div><h4>K40 Keystone Industrial Standard Carton</h4><p>K40 Keystone Industrial Standard Carton Sealing Tape is the industry standard for sealing medium […]</p></article>
      <article class="product-card"><div class="product-img" role="img" aria-label="Product photo of a case erector"></div><h4>Brightline CE-12 Case Erector</h4><p>The Brightline CE-12 Case Erector is a low-cost machine with an ergonomic design […]</p></article>
      <article class="product-card"><div class="product-img" role="img" aria-label="Product photo of a labeler"></div><h4>Pinebrook PB-20 Labeler</h4><p>The easy to use Pinebrook PB-20 Labeler is a compact and versatile label […]</p></article>
      <article class="product-card"><div class="product-img" role="img" aria-label="Product photo of a pallet labeler"></div><h4>Pinebrook PB-60 Pallet Labeler</h4><p>The Pinebrook PB-60 Pallet Labeler was designed and built with the palletizing […]</p></article>
      <article class="product-card"><div class="product-img" role="img" aria-label="Product photo of a shrink heat tunnel"></div><h4>Shrink Heat Tunnel HT-2/HT-3/HT-4</h4><p>Bad packages are caused by poor or uneven heat transfer to the shrink film […]</p></article>
    </div>
  </div>
</section>

<section class="newsletter">
  <h2>NEWSLETTER</h2>
  <p class="sub">Subscribe to Our Newsletter for Latest Updates</p>
  <div class="news-form">
    <div class="news-input">Email...</div>
    <span class="btn-dark">Subscribe »</span>
  </div>
</section>

<section class="testimonials">
  <div class="side-arrow" style="left:120px;top:212px"><svg width="8" height="8" viewBox="0 0 8 8"><path d="M6 1L2 4l4 3" fill="none" stroke="#777" stroke-width="1.5"/></svg></div>
  <div class="side-arrow" style="right:120px;top:212px"><svg width="8" height="8" viewBox="0 0 8 8"><path d="M2 1l4 3-4 3" fill="none" stroke="#777" stroke-width="1.5"/></svg></div>
  <div class="wrap">
    <h2 class="section-title">TESTIMONIALS</h2>
    <svg class="title-mark" viewBox="0 0 70 8"><path d="M0 4h26M44 4h26" stroke="#b3182c" stroke-width="1.5"/><rect x="30" y="1" width="10" height="6" fill="#b3182c"/></svg>
    <div class="testi-grid">
      <div>
        <div class="testi-card"><span class="quote-mark">“</span>Their team set up our new wrapper in one day and trained every shift operator before leaving. Service calls are answered the same morning, parts arrive quickly, and our line has rarely stopped since. We now buy all tape, film and labels from them as well.</div>
        <div class="testi-person"><div class="avatar" role="img" aria-label="Portrait photo of the client"></div><div><strong>DANA WHITFIELD</strong><span>Office Executive</span></div></div>
      </div>
      <div>
        <div class="testi-card"><span class="quote-mark">“</span>We replaced two old case erectors with their help and gained real speed on the floor. The technicians know the machines well, the maintenance plan keeps costs low, and the staff always finds the right supply for each job. A dependable name for our plant.</div>
        <div class="testi-person"><div class="avatar" role="img" aria-label="Portrait photo of the client"></div><div><strong>MARCUS HALE</strong><span>M.D.</span></div></div>
      </div>
    </div>
  </div>
</section>

<section class="brands">
  <div class="side-arrow" style="left:120px;top:148px"><svg width="8" height="8" viewBox="0 0 8 8"><path d="M6 1L2 4l4 3" fill="none" stroke="#777" stroke-width="1.5"/></svg></div>
  <div class="side-arrow" style="right:120px;top:148px"><svg width="8" height="8" viewBox="0 0 8 8"><path d="M2 1l4 3-4 3" fill="none" stroke="#777" stroke-width="1.5"/></svg></div>
  <h2 class="section-title">OUR BRANDS</h2>
  <svg class="title-mark" viewBox="0 0 70 8"><path d="M0 4h26M44 4h26" stroke="#b3182c" stroke-width="1.5"/><rect x="30" y="1" width="10" height="6" fill="#b3182c"/></svg>
  <div class="wrap brand-row">
    <span class="brand-name"><i></i>Corvane</span>
    <span class="brand-name">Tessly</span>
    <span class="brand-name"><i></i>Brenmark</span>
    <span class="brand-name">Ardell</span>
    <span class="brand-name"><i></i>Quillon</span>
    <span class="brand-name">Norstead</span>
  </div>
</section>

<footer class="footer">
  <div class="wrap">
    <div>
      <h5>CONTACT US</h5>
      <div class="f-list">
        <div><svg width="10" height="12" viewBox="0 0 10 12"><path d="M5 11S1 6.5 1 4.5a4 4 0 018 0C9 6.5 5 11 5 11z" fill="#fff"/></svg>2280 W Cedar Row Rd,<br>Millbrook, KS</div>
        <div><svg width="10" height="10" viewBox="0 0 10 10"><path d="M2 1l2 2-1 1.5c.8 1.4 1.7 2.3 3 3L7.5 6l2 2-1 1.5C4.5 9 1 5.5.5 1.5z" fill="#fff"/></svg>(555) 014 2290</div>
        <div><svg width="10" height="8" viewBox="0 0 10 8"><rect x=".5" y=".5" width="9" height="7" fill="none" stroke="#fff"/><path d="M.5.5l4.5 4 4.5-4" fill="none" stroke="#fff"/></svg>sales@halvernpack.com</div>
      </div>
      <div class="badge" role="img" aria-label="Chamber of commerce member badge"></div>
    </div>
    <div>
      <h5>QUICK CONTACT</h5>
      <div style="margin-top:10px">
        <div class="field">Name...</div>
        <div class="field">Email...</div>
        <div class="field tall">Message...</div>
        <span class="submit">SUBMIT</span>
      </div>
    </div>
    <div>
      <h5>FAQ</h5>
      <div class="faq-item"><div class="faq-thumb" role="img" aria-label="Machine photo"></div>Stratos W-240 "Machine Does Not Power Up</div>
      <div class="faq-item"><div class="faq-thumb" role="img" aria-label="Machine photo"></div>Strap jammed in head guides or around feed and take-up wheels</div>
      <div class="faq-item"><div class="faq-thumb" role="img" aria-label="Machine photo"></div>During Folding or Filling Cycle Box Releases, All Flaps Drop</div>
    </div>
    <div>
      <h5>LOCATE US</h5>
      <div class="map" role="img" aria-label="Map showing the company location in Kansas"></div>
    </div>
  </div>
</footer>
<div class="bottom-bar">
  <div class="wrap">
    <span>©Copyright information here | Designed by Studio</span>
    <div class="soc"><i></i><i style="background:#2a9ad8"></i><i style="background:#c9402f"></i><i style="background:#1f6aa8"></i></div>
  </div>
</div>
<div class="to-top"><svg width="12" height="10" viewBox="0 0 12 10"><path d="M1 8l5-5 5 5" fill="none" stroke="#fff" stroke-width="2"/></svg></div>

</body>
</html>
```